Cafe menu design

Hi there,

We need a editable menu layout and design to match our new cafe call: " Harlow Bean Roasters", we love the ideas of A4 clip board and self print out menu in black and white. ( Example as attached)

We would like the menu can be break down into category easy for customer to flip around and read. ( example as attached)

Category including the following:

- All day breakfast and Sandwich and Toast
- Main (Lunch&Dinner) and Pizza
- Dessert snacks and nibbles
- Hot and Cold Drinks
- Catering menu

Please find our logo and our current menu as attached for your information and convenience.
Updates

Dear Designers, Thank you for your time and submission, Please find our drink menu and logo as attached. Kind Regards,

Target Market(s)

Young family, young Couple, office and corporate staff

Industry/Entity Type

Cafe

Font styles to use
Serif
Sans Serif

```html
<!DOCTYPE html>
<html lang="en">
<head>
<meta charset="utf-8">
<title>Harlow Bean Roasters – Menu</title>
<link rel="stylesheet" href="https://fonts.googleapis.com/css2?family=Open+Sans:wght@400;700&family=Roboto+Slab:wght@700&family=Arimo:wght@700&display=swap">
<style>
  :root {
    --backdrop: #e6e8ea;
    --ink: #1b1b1b;
    --cover-dark: #232323;
    --cover-light: #ffffff;
    --paper: #ffffff;
    --rule: #555555;
    --ornament: #8a8a8a;
    --ornament-light: #cfcfcf;
  }
  * { box-sizing: border-box; margin: 0; padding: 0; }
  html, body {
    width: 1200px; height: 900px; overflow: hidden;
    background: var(--backdrop);
    font-family: "Open Sans", Arial, sans-serif;
    color: var(--ink);
  }
  .spread {
    position: relative; width: 1200px; height: 900px;
    display: flex; justify-content: center; align-items: center; gap: 90px;
  }
  .page {
    width: 400px; height: 566px; background: var(--paper);
    box-shadow: 0 2px 10px rgba(0,0,0,0.15);
    position: relative; overflow: hidden;
  }

  /* Cover */
  .cover__panel {
    position: absolute; inset: 0 0 80px 0; background: var(--cover-dark);
    color: var(--cover-light); text-align: center;
  }
  .cover__brand {
    margin-top: 70px; display: flex; flex-direction: column; align-items: center; gap: 14px;
  }
  .cover__brand-dot {
    width: 90px; height: 90px; border-radius: 50%; border: 3px solid var(--cover-light);
  }
  .cover__brand-name {
    font-family: "Open Sans", Arial, sans-serif; font-weight: 700;
    font-size: 24px; letter-spacing: 2px; text-transform: uppercase; line-height: 1.25;
  }
  .cover__ornament {
    margin: 0 auto; width: 140px; height: 34px;
    background: linear-gradient(90deg, transparent, var(--ornament-light), transparent);
    border-radius: 17px; opacity: .8;
  }
  .cover__ornament--top { margin-top: 38px; }
  .cover__title-block {
    margin: 6px 30px; border-top: 1px solid var(--cover-light);
    border-bottom: 1px solid var(--cover-light); padding: 18px 0;
  }
  .cover__title { font-size: 34px; font-weight: 400; letter-spacing: 1px; }
  .cover__foot {
    position: absolute; left: 0; right: 0; bottom: 0; height: 80px; padding: 4px 24px;
  }
  .cover__note { font-size: 8px; color: var(--rule); }

  /* Shared footer */
  .page__rules { width: 70px; margin: 14px auto 0; }
  .page__rules span { display: block; height: 1px; background: var(--rule); margin-bottom: 3px; }
  .page__tag {
    position: absolute; right: 22px; bottom: 14px;
    font-family: "Arimo", Arial, sans-serif; font-weight: 700; font-size: 19px; letter-spacing: -0.5px;
  }

  /* Inner */
  .inner { padding: 16px 26px 0; }
  .inner__flourish {
    margin: 0 auto; width: 250px; height: 30px;
    background: linear-gradient(90deg, transparent, var(--ornament), transparent);
    border-radius: 15px; opacity: .55;
  }
  .inner__heading {
    font-family: "Roboto Slab", Georgia, serif; font-weight: 700; font-size: 23px;
    text-align: center; margin-top: 4px; letter-spacing: .5px;
  }
  .inner__sub { text-align: center; font-weight: 700; font-size: 11px; }
  .inner__intro {
    text-align: center; font-size: 8px; font-weight: 700;
    border-bottom: 1px solid var(--rule); padding-bottom: 3px; margin-bottom: 4px;
  }
  .menu-list { list-style: none; font-size: 8.6px; line-height: 1.32; }
  .menu-item { display: flex; justify-content: space-between; gap: 8px; }
  .menu-item__name { font-weight: 700; }
  .menu-item__price { font-weight: 700; white-space: nowrap; }
  .menu-item__detail { padding-left: 10px; }
  .menu-item__note { font-size: 8px; }
  .menu-group { margin-top: 5px; }
</style>
</head>
<body>
<main class="spread">

  <section class="page cover" aria-label="Menu cover">
    <div class="cover__panel">
      <div class="cover__brand">
        <span class="cover__brand-dot" aria-hidden="true"></span>
        <span class="cover__brand-name">Harlow Bean<br>Roasters</span>
      </div>
      <div class="cover__ornament cover__ornament--top" role="img" aria-label="Decorative leaf flourish"></div>
      <div class="cover__title-block"><h1 class="cover__title">MENU</h1></div>
      <div class="cover__ornament" role="img" aria-label="Decorative leaf flourish"></div>
    </div>
    <div class="cover__foot">
      <p class="cover__note">With Tasmania smoked salmon OR breakfast sausage</p>
      <div class="page__rules"><span></span><span></span><span></span></div>
    </div>
    <p class="page__tag">all day breakfast.</p>
  </section>

  <section class="page inner" aria-label="All day breakfast">
    <div class="inner__flourish" role="img" aria-label="Decorative scroll flourish"></div>
    <h2 class="inner__heading">ALL DAY BREAKFAST</h2>
    <p class="inner__sub">Please order at counter</p>
    <p class="inner__intro">We use sourdough, panini and brioche buns from The Crust &amp; Crumb Co</p>
    <ul class="menu-list">
      <li class="menu-item"><span class="menu-item__name">Sourdough toast with butter/ jam/peanut butter/Yeast Spread</span></li>
      <li class="menu-item__detail">Cranberry, raisin &amp; fig</li>
      <li class="menu-item__detail">Wholemeal</li>
      <li class="menu-item"><span class="menu-item__name">Toasted fruit loaf with butter</span><span class="menu-item__price">1 for 3, 2 for 5</span></li>
      <li class="menu-item__detail">Banana bread</li>
      <li class="menu-item__detail">Fruit &amp; nut bread</li>
      <li class="menu-item__detail">Blueberry banana bread</li>
      <li class="menu-item__detail">Pear &amp; raspberry bread</li>
      <li class="menu-item menu-group"><span class="menu-item__name">Pancake with maple syrup, vanilla ice cream &amp; fresh cut banana</span><span class="menu-item__price">5</span></li>
      <li class="menu-item"><span class="menu-item__name">Poppy seed / blueberry bagel with cream cheese</span></li>
      <li class="menu-item"><span class="menu-item__name">Poppy seed bagel with smoked Tasmania salmon &amp; cream cheese</span><span class="menu-item__price">15</span></li>
      <li class="menu-item"><span class="menu-item__name">Low fat Greek yogurt</span><span class="menu-item__price">5</span></li>
      <li class="menu-item__note">with banana, toasted muesli, honey &amp; cinnamon</li>
      <li class="menu-item menu-group"><span class="menu-item__name">Smoked ham &amp; tasty cheese croissant</span><span class="menu-item__price">9</span></li>
      <li class="menu-item"><span class="menu-item__name">Tasty cheese &amp; tomato croissant</span><span class="menu-item__price">8</span></li>
      <li class="menu-item"><span class="menu-item__name">Date Scone with jam &amp; fresh cream</span></li>
      <li class="menu-item"><span class="menu-item__name">Wholemeal sourdough sandwiches</span></li>
      <li class="menu-item menu-item__detail"><span>- Turkey, rocket &amp; cranberry</span><span class="menu-item__price">6.5</span></li>
      <li class="menu-item menu-item__detail"><span>- Leg ham, cheese, avocado &amp; rocket</span><span class="menu-item__price">6.5</span></li>
      <li class="menu-item menu-item__detail"><span>- Smoked salmon, feta, avocado &amp; rocket</span><span class="menu-item__price">4.5</span></li>
      <li class="menu-item menu-item__detail"><span>- Sicilian tuna, boiled eggs &amp; rocket</span><span class="menu-item__price">8.5</span></li>
      <li class="menu-item__detail">- Char-grilled eggplant &amp; zucchini, feta, pesto &amp; rocket</li>
      <li class="menu-item__detail">- Smoked chicken breast, cheese, avocado &amp; rocket</li>
      <li class="menu-item menu-group"><span class="menu-item__name">Hash brown, grilled haloumi, green olive, sourdough &amp; lemon wedge</span><span class="menu-item__price">15</span></li>
      <li class="menu-item__note">With Tasmania smoked salmon OR breakfast sausage</li>
    </ul>
    <div class="page__rules"><span></span><span></span><span></span></div>
    <p class="page__tag">all day breakfast.</p>
  </section>

</main>
</body>
</html>
```